Re-design of 4 x 2-sided reports

I need the 4 attached reports (3 are 2-sides of A4; 1 is 7-sides of A4) to be re-designed with a consistent look and feel. Just need 1 or 2 images per report being inserted plus consistent branding and contact details being displayed in the same location on each report with same colour, font and design). Reports are attached.
The reports are used as lead magnets.
That is, visitors to our website can download one of them (7 Steps To Sharpen Your Sales Over The Coming Month) by filling in a form with their email address. Then over the next 30 days the other reports are sent to the subscriber via email autoresponders.
Blue Harbour Marketing is a marketing consultancy dealing with companies in the North West of England providing cost-effective and profitable marketing to small and medium-sized businesses that want better and quicker results. The reports need to be professional and corporate looking. Please let me know if you need any further clarification or have any questions. I attach an example report. I don't necessarily want to mirror this report (from the law firm) but it may help to understand what look I'm trying to get. Many thanks, Gordon

Target Market(s)

SMEs based in NW of England
Typically with turnover of £1m to £10m or 10 to 100 employees
Clients often in the construction sector, healthcare, accountants, lawyers and local councils.

Industry/Entity Type

Marketing

Font styles to use
Serif
Sans Serif

Colors
ec1f27

Requirements
Must have
• Consistent branding
• Logo in same place across all four reports
• Contact details in same place across all four reports
• Same font across all four reports
• Same colour across all four reports
• Professional and bold look
Nice to have
• Some strong stock photography
• 1 or 2 images per report
• More images for the 7-page report though
Should not have
• No graphics

```html
<!DOCTYPE html>
<html lang="en">
<head>
<meta charset="utf-8">
<title>17 Reasons To Use Press Releases – Report Covers</title>
<link href="https://fonts.googleapis.com/css2?family=Arimo:wght@400;700&family=Open+Sans:ital,wght@0,400;0,700;1,400&display=swap" rel="stylesheet">
<style>
  :root {
    --brand-red: #c8202a;
    --ink: #2b2b2b;
    --paper: #ffffff;
    --backdrop: #5a6a5b;
    --rule: #3a3a3a;
    --tablet-tone-a: #b9bbbe;
    --tablet-tone-b: #8f9296;
    --crowd-tone-a: #5e7280;
    --crowd-tone-b: #a9b7bd;
  }
  * { margin: 0; padding: 0; box-sizing: border-box; }
  html, body { width: 922px; height: 1200px; overflow: hidden; }
  body {
    background: var(--backdrop);
    display: flex;
    flex-direction: column;
    align-items: center;
    justify-content: center;
    gap: 30px;
    font-family: "Arimo", Arial, sans-serif;
  }
  .report-cover {
    width: 400px;
    height: 566px;
    background: var(--paper);
    display: flex;
    flex-direction: column;
    box-shadow: 0 4px 14px rgba(0,0,0,0.25);
  }
  .cover-header {
    height: 166px;
    display: flex;
    align-items: center;
    padding: 0 30px 0 40px;
    gap: 22px;
  }
  .brand-mark {
    width: 92px;
    display: flex;
    flex-direction: column;
    align-items: center;
    gap: 6px;
  }
  .brand-square {
    width: 64px;
    height: 64px;
    background: var(--brand-red);
  }
  .brand-name {
    font-family: "Arimo", Arial, sans-serif;
    font-size: 12px;
    line-height: 1.15;
    color: var(--brand-red);
    text-align: center;
  }
  .cover-title {
    line-height: 1.18;
    font-size: 20px;
  }
  .cover-title .count { color: var(--ink); font-weight: 400; display: block; }
  .cover-title .strong { color: var(--brand-red); font-weight: 700; display: block; }
  .cover-title .light { color: var(--brand-red); font-weight: 400; display: block; }
  .cover-image { height: 312px; }
  .cover-image.tablet {
    background: linear-gradient(180deg, var(--tablet-tone-a), var(--tablet-tone-b));
  }
  .cover-image.megaphone {
    background: linear-gradient(160deg, var(--crowd-tone-a), var(--crowd-tone-b) 60%, #7d8c93);
  }
  .cover-footer {
    flex: 1;
    display: flex;
    flex-direction: column;
    align-items: center;
    padding-top: 16px;
    font-family: "Open Sans", Arial, sans-serif;
  }
  .footer-url {
    color: var(--brand-red);
    font-weight: 700;
    font-size: 10px;
  }
  .footer-rule {
    width: 120px;
    border-top: 1px solid var(--rule);
    margin: 12px 0 8px;
  }
  .footer-note {
    font-style: italic;
    font-size: 9.5px;
    color: var(--ink);
  }
  .footer-copyright {
    font-size: 5.5px;
    color: var(--ink);
    margin-top: 3px;
  }
</style>
</head>
<body>
  <article class="report-cover">
    <header class="cover-header">
      <div class="brand-mark">
        <div class="brand-square"></div>
        <div class="brand-name">Blue Harbour Marketing</div>
      </div>
      <h1 class="cover-title">
        <span class="count">17 Reasons</span>
        <span class="strong">To Use Press Releases</span>
        <span class="light">To Promote</span>
        <span class="strong">Your Business</span>
      </h1>
    </header>
    <div class="cover-image tablet" role="img" aria-label="Photo of two hands holding a tablet showing a press release page with charts, over a grey network-map background"></div>
    <footer class="cover-footer">
      <p class="footer-url">www.BlueHarbourMarketing.co.uk</p>
      <div class="footer-rule"></div>
      <p class="footer-note">Your “Blue Harbour Marketing” FREE Report</p>
      <p class="footer-copyright">© Copyright 2016 Blue Harbour Marketing, All Rights Reserved</p>
    </footer>
  </article>

  <article class="report-cover">
    <header class="cover-header">
      <div class="brand-mark">
        <div class="brand-square"></div>
        <div class="brand-name">Blue Harbour Marketing</div>
      </div>
      <h1 class="cover-title">
        <span class="count">17 Reasons</span>
        <span class="strong">To Use Press Releases</span>
        <span class="light">To Promote</span>
        <span class="strong">Your Business</span>
      </h1>
    </header>
    <div class="cover-image megaphone" role="img" aria-label="Photo of a businessman shouting through a megaphone with letters flying out under a stormy sky"></div>
    <footer class="cover-footer">
      <p class="footer-url">www.BlueHarbourMarketing.co.uk</p>
      <div class="footer-rule"></div>
      <p class="footer-note">Your “Blue Harbour Marketing” FREE Report</p>
      <p class="footer-copyright">© Copyright 2016 Blue Harbour Marketing, All Rights Reserved</p>
    </footer>
  </article>
</body>
</html>
```